Private Maths Tuition Flyer based in London

I am opening up a new Maths tuition centre in North West London. The flyer will be delivered to over 8,000 homes within the immediate vicinity. The design should be suitable to be printed on an A5 sheet and read in a portrait orientation.

The flyer should include the following:

The headline statement should be "Private Maths Tuition"

Secondary headline statement is the following "GCSE, A-Levels, 11 Plus exams"

Some of service offerings/selling points are:

- Free first session
- Monthly Feedback reports
- Free support outside of sessions
- Clear Target grades
- Personalised Lesson plans
- Tangible Results

Another statement that should be featured is "Book your free session by visiting www.lernova.co.uk" or something similar to that.

"Contact Details:
020 7418 2903
enquiries@lernova.co.uk"

"Address:
Corbel Business and Innovation Centre
Wyvern Court
Larkfield Road
HA9 4QW"

Attached you'll see a logo which should be included and also a map of where we are. I am open to new images for the map if you guys have any, rather than a screen shot from plotway atlas but it should be clear to see.

I would like the content above to be displayed in a clear and concise manner that is easy to read. You have creative license on where this information should be displayed and where the images should be but on the whole it should look aesthetically pleasing on the eye.

Target Market(s)

Students, Parents. Parents who want maths tutors.

Industry/Entity Type

Tutoring

Font styles to use
Sans Serif

Requirements
Must have
• *logo*
• Private Maths Tuition
• GCSE, A-Levels, 11 Plus exams
• - Free first session
• - Monthly Feedback reports
• - Free support outside of sessions
• - Clear Target grades
• - Personalised Lesson plans
• - Tangible Results
• Book your free session by visiting www.lernova.co.uk" or something similar to that.
• Contact Details:
• 020 7418 2903
• enquiries@lernova.co.uk
• Address (*with map*):
• Corbel Business and Innovation Centre
• Wyvern Court
• Larkfield Road
• HA9 4QW
Nice to have
• similar colour scheme as the logo. creative background design.

```html
<!DOCTYPE html>
<html lang="en">
<head>
<meta charset="utf-8">
<title>Private Maths Tuition – Lernova</title>
<link rel="stylesheet" href="https://fonts.googleapis.com/css2?family=Open+Sans:wght@400;600;700&display=swap">
<style>
  :root {
    --blue: #1d71b8;
    --blue-deep: #1957a6;
    --orange: #f07122;
    --charcoal: #3c3c3e;
    --slate: #6d6e71;
    --ink: #333333;
    --paper: #ffffff;
    --backdrop: #ececea;
    --wood-light: #d9ae78;
    --wood-mid: #b07f4b;
    --wood-dark: #5e3d22;
    --note-white: #f3efe6;
    --mug-red: #b8322a;
    --map-base: #ebe8e1;
    --map-road: #ffffff;
    --map-green: #cfe3b6;
    --pin-red: #d9453b;
    --pin-text: #a3231c;
  }
  * { box-sizing: border-box; margin: 0; padding: 0; }
  html, body {
    width: 948px; height: 1200px; overflow: hidden;
    background: var(--backdrop);
    font-family: "Open Sans", sans-serif;
  }
  .flyer {
    position: absolute; left: 78px; top: 40px;
    width: 585px; height: 828px;
    background: var(--paper);
    transform: scale(1.3536); transform-origin: top left;
    overflow: hidden;
  }
  .headline {
    position: absolute; top: 18px; left: 0; width: 100%;
    text-align: center; color: var(--blue);
    font-weight: 700; font-size: 40px; letter-spacing: 0.2px; line-height: 48px;
  }
  .subhead {
    position: absolute; top: 66px; left: 0; width: 100%;
    text-align: center; color: var(--ink);
    font-weight: 600; font-size: 19px;
  }
  .rule { position: absolute; left: 0; width: 100%; height: 5px; background: var(--charcoal); }
  .rule--top { top: 116px; }
  .rule--bottom { top: 467px; }
  .photo {
    position: absolute; top: 121px; left: 0; width: 585px; height: 346px;
    background:
      radial-gradient(ellipse 170px 90px at 300px 290px, var(--note-white) 0%, rgba(243,239,230,0.55) 55%, rgba(243,239,230,0) 100%),
      radial-gradient(ellipse 38px 44px at 360px 50px, rgba(184,50,42,0.85) 0%, rgba(184,50,42,0) 100%),
      radial-gradient(ellipse 60px 80px at 560px 60px, rgba(240,238,232,0.9) 0%, rgba(240,238,232,0) 100%),
      radial-gradient(ellipse 120px 160px at 545px 250px, rgba(150,95,70,0.6) 0%, rgba(150,95,70,0) 100%),
      radial-gradient(ellipse at 40% 20%, var(--wood-light) 0%, var(--wood-mid) 50%, var(--wood-dark) 100%);
  }
  .corner { position: absolute; }
  .corner--orange { top: 103px; right: 0; }
  .corner--blue { top: 405px; left: 0; }

  .brand {
    position: absolute; top: 552px; left: 34px;
    display: flex; align-items: center; gap: 10px;
  }
  .brand__dot { width: 18px; height: 18px; border-radius: 50%; background: var(--blue); }
  .brand__name { font-size: 36px; font-weight: 600; color: var(--orange); line-height: 1; }

  .benefits { position: absolute; top: 620px; left: 24px; list-style: none; }
  .benefits li {
    position: relative; padding-left: 13px;
    font-size: 15.5px; font-weight: 600; color: var(--ink); line-height: 23px;
  }
  .benefits li::before {
    content: ""; position: absolute; left: 0; top: 6px;
    border-left: 7px solid var(--blue-deep);
    border-top: 5px solid transparent; border-bottom: 5px solid transparent;
  }

  .contact { position: absolute; left: 0; top: 775px; width: 313px; height: 53px; }
  .contact__text {
    position: absolute; top: 8px; left: 26px;
    color: var(--paper); font-size: 14px; font-weight: 600; line-height: 19px;
  }

  .location { position: absolute; top: 472px; left: 313px; width: 272px; height: 356px; background: var(--slate); }
  .booking {
    position: absolute; top: 493px; left: 299px; width: 286px; height: 49px;
    background: var(--orange); color: var(--paper); text-align: center;
  }
  .booking__lead { font-size: 12.5px; padding-top: 6px; line-height: 17px; }
  .booking__url {
    display: flex; justify-content: center; align-items: center; gap: 6px;
    font-size: 13px; font-weight: 700; line-height: 20px;
  }
  .map {
    position: absolute; top: 542px; left: 313px; width: 272px; height: 218px;
    background:
      radial-gradient(ellipse 70px 60px at 60px 170px, var(--map-green) 0%, rgba(207,227,182,0) 100%),
      radial-gradient(ellipse 40px 50px at 250px 50px, var(--map-green) 0%, rgba(207,227,182,0) 100%),
      radial-gradient(ellipse 140px 60px at 150px 100px, rgba(255,255,255,0.7) 0%, rgba(255,255,255,0) 100%),
      var(--map-base);
  }
  .map__marker { position: absolute; left: 145px; top: 84px; }
  .map__label {
    position: absolute; left: 157px; top: 98px;
    font-size: 6.5px; font-weight: 700; line-height: 8px; color: var(--pin-text);
  }
  .address {
    position: absolute; top: 760px; left: 313px; width: 272px; height: 53px;
    background: var(--slate); color: var(--paper);
    display: flex; align-items: center; gap: 10px; padding-left: 36px;
    font-size: 10px; line-height: 15px;
  }
  .address-strip { position: absolute; top: 813px; left: 313px; width: 272px; height: 15px; background: var(--blue-deep); }
</style>
</head>
<body>
  <main class="flyer">
    <h1 class="headline">PRIVATE MATHS TUITION</h1>
    <p class="subhead">GCSE, A-Levels, 11 Plus exams</p>

    <div class="photo" role="img" aria-label="Photo of a hand writing maths notes on a wooden desk beside glasses and a red mug"></div>
    <div class="rule rule--top"></div>
    <svg class="corner corner--orange" width="118" height="82" viewBox="0 0 118 82" aria-hidden="true">
      <polygon points="0,0 118,0 118,82" fill="var(--orange)"/>
    </svg>
    <svg class="corner corner--blue" width="104" height="80" viewBox="0 0 104 80" aria-hidden="true">
      <polygon points="0,0 0,80 104,80" fill="var(--blue)"/>
    </svg>
    <div class="rule rule--bottom"></div>

    <div class="location"></div>
    <div class="booking">
      <p class="booking__lead">Book your free session by visiting</p>
      <p class="booking__url">
        <svg width="12" height="12" viewBox="0 0 12 12" aria-hidden="true">
          <circle cx="6" cy="6" r="4.5" fill="none" stroke="var(--paper)" stroke-width="1.8"/>
          <path d="M7 6 L11 11" stroke="var(--paper)" stroke-width="1.8"/>
        </svg>
        www.lernova.co.uk
      </p>
    </div>
    <div class="map" role="img" aria-label="Street map showing the location of Corbel Business and Innovation Centre">
      <svg class="map__marker" width="10" height="14" viewBox="0 0 10 14" aria-hidden="true">
        <path d="M5 0 C2.2 0 0 2.2 0 5 C0 8.5 5 14 5 14 C5 14 10 8.5 10 5 C10 2.2 7.8 0 5 0 Z" fill="var(--pin-red)"/>
        <circle cx="5" cy="5" r="1.8" fill="var(--pin-text)"/>
      </svg>
      <p class="map__label">Corbel Business<br>and Innovation Centre</p>
    </div>
    <div class="address">
      <svg width="10" height="14" viewBox="0 0 10 14" aria-hidden="true">
        <path d="M5 0 C2.2 0 0 2.2 0 5 C0 8.5 5 14 5 14 C5 14 10 8.5 10 5 C10 2.2 7.8 0 5 0 Z" fill="var(--paper)"/>
        <circle cx="5" cy="5" r="1.8" fill="var(--slate)"/>
      </svg>
      <p>Corbel Business and Innovation Centre<br>Wyvern Court Larkfield Road HA9 4QW</p>
    </div>
    <div class="address-strip"></div>

    <div class="brand">
      <span class="brand__name">Lernova</span>
      <span class="brand__dot"></span>
    </div>

    <ul class="benefits">
      <li>Free first session</li>
      <li>Monthly Feedback reports</li>
      <li>Free support outside of sessions</li>
      <li>Clear Target grades</li>
      <li>Personalised Lesson plans</li>
      <li>Tangible Results</li>
    </ul>

    <div class="contact">
      <svg width="313" height="53" viewBox="0 0 313 53" aria-hidden="true">
        <polygon points="0,0 268,0 313,45 313,53 0,53" fill="var(--blue-deep)"/>
      </svg>
      <p class="contact__text">020 7418 2903<br>enquiries@lernova.co.uk</p>
    </div>
  </main>
</body>
</html>
```